NestaDwell product hardcopy flyer design

Design an A4 flyer for a microhome. We build mobile dwellings (www.nestadwellco.com.au) so need a flyer to hand to people which shows some floor layout options, the design and purchase process, etc. Aim is to draw inspiration from the website with a clean feel that primarily highlights the design and build process, as well as the four main design options we build and offer.

Industry/Entity Type

Building

Font styles to use
Sans Serif

Colors
00a990

Requirements
Must have
• a section detailing the design process
• a section showing the various microhome options
Nice to have
• a clean feel, similiar to the website - www.nestadwellco.com.au
Should not have
• any reference to the word tiny house, or tiny home

```html
<!DOCTYPE html>
<html lang="en">
<head>
<meta charset="UTF-8">
<title>NestaDwell – A Home For Under 70K</title>
<link href="https://fonts.googleapis.com/css2?family=Montserrat:wght@300;400;600&family=Open+Sans:wght@400;600;700&display=swap" rel="stylesheet">
<style>
  :root {
    --teal: #00a990;
    --ink: #1c1c1c;
    --text: #3a3a3a;
    --white: #ffffff;
    --label-bg: #3b3b3b;
    --footer-bg: #000000;
    --footer-text: #d8d8d8;
  }
  html, body { margin: 0; padding: 0; overflow: hidden; background: var(--white); }
  .flyer {
    position: relative;
    width: 849px; height: 1200px;
    overflow: hidden;
    background: var(--white);
    font-family: "Open Sans", Arial, sans-serif;
    color: var(--text);
  }
  .hero-photo {
    position: absolute; left: 0; top: 0; width: 849px; height: 480px;
    background: linear-gradient(180deg, #d9dcd8 0%, #c7cbc6 18%, #5f6b55 45%, #4c5a3e 62%, #6d7a4b 80%, #7b8753 100%);
  }
  .hero-curve { position: absolute; left: 0; top: 200px; width: 849px; height: 290px; }
  .hero-headline {
    position: absolute; left: 0; top: 170px; width: 849px; text-align: center;
    font-family: "Montserrat", Arial, sans-serif;
  }
  .hero-headline .lead {
    display: block; color: var(--white); font-weight: 400;
    font-size: 40px; letter-spacing: 10px;
  }
  .hero-headline .price {
    display: block; color: var(--teal); font-weight: 600;
    font-size: 76px; letter-spacing: 22px; margin-top: -6px;
  }
  .brand-mark {
    position: absolute; left: 0; top: 395px; width: 849px;
    display: flex; justify-content: center; align-items: center; gap: 12px;
    color: var(--teal); font-weight: 600; font-size: 32px;
  }
  .brand-mark .dot { width: 18px; height: 18px; border-radius: 50%; background: var(--teal); }
  .section-title {
    position: absolute; left: 38px; margin: 0;
    font-family: "Montserrat", Arial, sans-serif; font-weight: 400;
    font-size: 25px; letter-spacing: 6px; color: var(--ink);
  }
  .collection-title { top: 478px; }
  .steps-title { top: 726px; }
  .collection {
    position: absolute; top: 535px; left: 38px; width: 774px;
    display: flex; justify-content: space-between;
  }
  .model-card { width: 185px; }
  .model-card .model-photo { height: 125px; }
  .model-card .model-name {
    height: 27px; line-height: 27px; background: var(--label-bg);
    color: var(--white); font-weight: 700; font-size: 17px; text-align: center;
  }
  .photo-urban { background: linear-gradient(180deg, #cfd8e0 0%, #e8eaec 45%, #9aa48a 100%); }
  .photo-eco { background: linear-gradient(180deg, #6fa4d2 0%, #b8cfd8 45%, #7d7a66 100%); }
  .photo-offgrid { background: linear-gradient(180deg, #5c6b3e 0%, #7f8d58 50%, #56643a 100%); }
  .photo-bespoke { background: linear-gradient(180deg, #f1f3f5 0%, #c9d3df 50%, #3f5c9c 100%); }
  .steps {
    position: absolute; top: 770px; left: 30px; width: 790px;
    display: flex; justify-content: space-between;
  }
  .step { width: 192px; text-align: center; }
  .step .num {
    width: 26px; height: 26px; margin: 0 auto; border-radius: 50%;
    background: var(--ink); color: var(--white);
    font-weight: 700; font-size: 16px; line-height: 26px;
  }
  .step .icon { height: 70px; margin-top: 8px; }
  .step .icon svg { height: 66px; }
  .step h3 { margin: 12px 0 4px; font-size: 19px; font-weight: 700; color: var(--ink); }
  .step p { margin: 0; font-size: 13px; line-height: 16px; color: var(--text); }
  .footer-band { position: absolute; left: 0; top: 1020px; width: 849px; height: 180px; }
  .footer-brand {
    position: absolute; left: 40px; top: 1128px;
    display: flex; align-items: center; gap: 10px;
    color: var(--white); font-weight: 600; font-size: 22px;
  }
  .footer-brand .dot { width: 14px; height: 14px; border-radius: 50%; background: var(--white); }
  .contact {
    position: absolute; right: 37px; top: 1084px; text-align: right;
    color: var(--footer-text); font-size: 14px; line-height: 19px;
  }
  .contact .contact-name {
    color: var(--white); font-weight: 700; font-size: 18px;
    margin-bottom: 6px; text-align: left;
  }
  .contact p { margin: 0; }
</style>
</head>
<body>
<div class="flyer">
  <div class="hero-photo" role="img" aria-label="Photo of a grey clad microhome with deck and outdoor chairs on a grassy lot with trees behind"></div>
  <svg class="hero-curve" viewBox="0 200 849 290" preserveAspectRatio="none" aria-hidden="true">
    <path d="M0 450 Q424 226 849 450 L849 490 L0 490 Z" fill="#ffffff"/>
  </svg>

  <h1 class="hero-headline">
    <span class="lead">A HOME FOR UNDER</span>
    <span class="price">70K!</span>
  </h1>

  <div class="brand-mark"><span class="dot"></span>NestaDwell</div>

  <h2 class="section-title collection-title">OUR COLLECTION</h2>
  <div class="collection">
    <div class="model-card">
      <div class="model-photo photo-urban" role="img" aria-label="Urban model microhome with solar awning"></div>
      <div class="model-name">Urban</div>
    </div>
    <div class="model-card">
      <div class="model-photo photo-eco" role="img" aria-label="Eco model microhome rendering with deck"></div>
      <div class="model-name">Eco</div>
    </div>
    <div class="model-card">
      <div class="model-photo photo-offgrid" role="img" aria-label="Off-grid model microhome on a green hillside"></div>
      <div class="model-name">Off-Grid</div>
    </div>
    <div class="model-card">
      <div class="model-photo photo-bespoke" role="img" aria-label="Bespoke model cutaway floor layout rendering"></div>
      <div class="model-name">Bespoke</div>
    </div>
  </div>

  <h2 class="section-title steps-title">JUST FOUR STEPS!</h2>
  <div class="steps">
    <div class="step">
      <div class="num">1</div>
      <div class="icon">
        <svg viewBox="0 0 70 66" aria-hidden="true">
          <ellipse cx="26" cy="24" rx="24" ry="18" fill="#1c1c1c"/>
          <path d="M10 36 L6 50 L22 40 Z" fill="#1c1c1c"/>
          <ellipse cx="48" cy="40" rx="20" ry="15" fill="#1c1c1c" stroke="#fff" stroke-width="3"/>
          <path d="M58 50 L64 62 L50 53 Z" fill="#1c1c1c"/>
        </svg>
      </div>
      <h3>First Chat</h3>
      <p>Contact us to book a free project consultation and we can discuss your project in more detail.</p>
    </div>
    <div class="step">
      <div class="num">2</div>
      <div class="icon">
        <svg viewBox="0 0 60 66" aria-hidden="true">
          <rect x="6" y="8" width="40" height="54" rx="3" fill="none" stroke="#1c1c1c" stroke-width="4"/>
          <rect x="16" y="3" width="20" height="10" rx="2" fill="#1c1c1c"/>
          <line x1="13" y1="24" x2="38" y2="24" stroke="#1c1c1c" stroke-width="4"/>
          <line x1="13" y1="34" x2="30" y2="34" stroke="#1c1c1c" stroke-width="4"/>
          <line x1="13" y1="44" x2="26" y2="44" stroke="#1c1c1c" stroke-width="4"/>
          <circle cx="44" cy="48" r="13" fill="#fff" stroke="#1c1c1c" stroke-width="4"/>
          <path d="M37 48 L42 53 L51 43" fill="none" stroke="#1c1c1c" stroke-width="4"/>
        </svg>
      </div>
      <h3>The Plan</h3>
      <p>Once we’ve had the first chat we’ll put together a more detailed proposal, including costing.<br>A site inspection may also be carried out so that our team can assess accessibility.</p>
    </div>
    <div class="step">
      <div class="num">3</div>
      <div class="icon">
        <svg viewBox="0 0 66 66" aria-hidden="true">
          <line x1="12" y1="54" x2="48" y2="18" stroke="#1c1c1c" stroke-width="8" stroke-linecap="round"/>
          <path d="M40 8 L60 28 L52 30 L38 16 Z" fill="#1c1c1c"/>
          <line x1="18" y1="14" x2="54" y2="54" stroke="#1c1c1c" stroke-width="7" stroke-linecap="round"/>
          <circle cx="14" cy="12" r="9" fill="none" stroke="#1c1c1c" stroke-width="5"/>
        </svg>
      </div>
      <h3>Construction</h3>
      <p>All NestaDwell homes are built within our factory in Kelsbury, and we welcome your visits to check the progress. We will also update you via regular emails and images.</p>
    </div>
    <div class="step">
      <div class="num">4</div>
      <div class="icon">
        <svg viewBox="0 0 80 66" aria-hidden="true">
          <rect x="2" y="12" width="46" height="36" fill="#1c1c1c"/>
          <path d="M52 24 L66 24 L76 36 L76 48 L52 48 Z" fill="#1c1c1c"/>
          <circle cx="16" cy="52" r="7" fill="#fff" stroke="#1c1c1c" stroke-width="4"/>
          <circle cx="62" cy="52" r="7" fill="#fff" stroke="#1c1c1c" stroke-width="4"/>
        </svg>
      </div>
      <h3>Delivery</h3>
      <p>Contact us to book a free project consultation and we can discuss your project in more detail.</p>
    </div>
  </div>

  <svg class="footer-band" viewBox="0 1020 849 180" preserveAspectRatio="none" aria-hidden="true">
    <path d="M0 1035 Q424 1125 849 1035 L849 1200 L0 1200 Z" fill="#000000"/>
  </svg>

  <div class="footer-brand"><span class="dot"></span>NestaDwell</div>

  <div class="contact">
    <div class="contact-name">NestaDwell | Group</div>
    <p>Unit 14, 88 Larkfield Rd, Brenton 3199 VIC</p>
    <p>Telephone: 03 9000 4812</p>
    <p>Email: info@nestadwellco.com.au</p>
    <p>Website: www.nestadwellco.com.au</p>
  </div>
</div>
</body>
</html>
```